Need wine label for brand that is named: Casmerel Vineyards & Winery

Casmerel is a yoga way of breathing. In Sanskrit Casmerel means "flying up." I would like a creative wine label that articulates Casmerel. The label should include a graphic and the name Casmerel on one line and Vineyards & Winery in smaller print underneath Casmerel.

```html
<!DOCTYPE html>
<html lang="en">
<head>
<meta charset="utf-8">
<title>Casmerel Vineyards &amp; Winery – Wine Label</title>
<link rel="stylesheet" href="https://fonts.googleapis.com/css2?family=Marcellus&family=Cormorant+Garamond:ital,wght@0,500;1,400&family=Tangerine:wght@400&display=swap">
<style>
  :root {
    --backdrop: #1a181c;
    --label-white: #ffffff;
    --gold: #d4b000;
    --gold-deep: #b89400;
    --gold-soft: #f3e6a6;
    --ink: #1b1a1c;
  }
  * { margin: 0; padding: 0; box-sizing: border-box; }
  html, body {
    width: 1200px;
    height: 848px;
    overflow: hidden;
    background: var(--backdrop);
  }
  .canvas {
    position: relative;
    width: 1200px;
    height: 848px;
  }
  .wine-label {
    position: absolute;
    left: 389px;
    top: 173px;
    width: 413px;
    height: 467px;
    background: var(--label-white);
    overflow: hidden;
    text-align: center;
  }
  .side-pattern {
    position: absolute;
    top: 0;
    right: 0;
    width: 100%;
    height: 100%;
    background: linear-gradient(90deg,
      rgba(255,255,255,0) 0%,
      rgba(255,255,255,0) 48%,
      var(--gold-soft) 72%,
      var(--gold) 100%);
  }
  .brand-mark {
    position: absolute;
    left: 50%;
    top: 40px;
    width: 132px;
    height: 132px;
    margin-left: -66px;
    border-radius: 50%;
    background: radial-gradient(circle, var(--gold) 0%, var(--gold-deep) 100%);
  }
  .brand-name {
    position: absolute;
    left: 0;
    right: 0;
    top: 196px;
    font-family: "Marcellus", serif;
    font-size: 47px;
    letter-spacing: 4px;
    color: var(--ink);
    line-height: 1;
  }
  .brand-sub {
    position: absolute;
    left: 0;
    right: 0;
    top: 262px;
    font-family: "Cormorant Garamond", serif;
    font-weight: 500;
    font-size: 15px;
    letter-spacing: 3px;
    color: var(--ink);
  }
  .appellation {
    position: absolute;
    left: 0;
    right: 0;
    top: 290px;
    font-family: "Tangerine", cursive;
    font-size: 70px;
    color: var(--gold);
    line-height: 1;
  }
  .vintage {
    position: absolute;
    left: 0;
    right: 0;
    top: 352px;
    font-family: "Cormorant Garamond", serif;
    font-style: italic;
    font-size: 34px;
    letter-spacing: 5px;
    color: var(--ink);
    line-height: 1;
  }
  .volume {
    position: absolute;
    left: 0;
    right: 0;
    top: 436px;
    font-family: "Cormorant Garamond", serif;
    font-weight: 500;
    font-size: 15px;
    color: var(--ink);
  }
</style>
</head>
<body>
  <main class="canvas">
    <section class="wine-label">
      <div class="side-pattern" role="img" aria-label="Faint gold ornamental pattern fading in along the right edge"></div>
      <div class="brand-mark" aria-hidden="true"></div>
      <h1 class="brand-name">CASMEREL</h1>
      <p class="brand-sub">VINEYARDS &amp; WINERY</p>
      <p class="appellation">Napa Valley</p>
      <p class="vintage">2015</p>
      <p class="volume">13.5% alc./vol. 750ml</p>
    </section>
  </main>
</body>
</html>
```